Business Card Design

I have a very clear idea of what I want. I just do not know how to do the graphic design to match it.

On the front I want the uploaded image with the horse and the two people.
I want

Bottom left hand corner
Lenny Firth
0472 316 508

Bottom right
There is maroon block with Morris Tane Practitioner Group Logo
Next to that I want the Stable Arc tile about the same size ( attached psd file)

On the back I want a plain colour (white) with the information

Lenny Firth
Equine Performance
Brindle4Ponies and Acupuncture
Horsemanship Lessons and Clinics
Horse Training

lfirth@critterloop.com.au
FB/lenny.firth.263
StableArc.com.au

Lenny Firth
0472 316 508
lfirth@critterloop.com.au

```html
<!DOCTYPE html>
<html lang="en">
<head>
<meta charset="utf-8">
<title>Lenny Firth – Business Card Back</title>
<link rel="stylesheet" href="https://fonts.googleapis.com/css2?family=Libre+Baskerville:ital,wght@0,400;0,700;1,400&display=swap">
<style>
  :root {
    --card-bg: #ffffff;
    --ink: #2a1410;
  }
  html, body {
    margin: 0;
    padding: 0;
    width: 1200px;
    height: 741px;
    overflow: hidden;
    background: var(--card-bg);
  }
  .card-back {
    position: relative;
    width: 1200px;
    height: 741px;
    background: var(--card-bg);
    color: var(--ink);
    font-family: "Libre Baskerville", "Baskerville", Georgia, serif;
  }
  .services {
    position: absolute;
    left: 112px;
    top: 98px;
    margin: 0;
  }
  .services__name {
    margin: 0;
    font-size: 44px;
    font-weight: 700;
    line-height: 52px;
    letter-spacing: -0.3px;
  }
  .services__list {
    list-style: none;
    margin: 0;
    padding: 0;
  }
  .services__item {
    font-size: 35px;
    font-style: italic;
    line-height: 52px;
    letter-spacing: -0.4px;
  }
  .contact {
    position: absolute;
    left: 112px;
    top: 403px;
    margin: 0;
    font-style: normal;
    font-size: 31px;
    line-height: 43px;
    letter-spacing: -0.2px;
  }
  .contact span {
    display: block;
  }
</style>
</head>
<body>
  <main class="card-back">
    <section class="services">
      <h1 class="services__name">Lenny Firth</h1>
      <ul class="services__list">
        <li class="services__item">Equine Performance</li>
        <li class="services__item">Brindle4Ponies and Acupuncture</li>
        <li class="services__item">Horsemanship Lessons and Clinics</li>
        <li class="services__item">Horse Training</li>
      </ul>
    </section>
    <address class="contact">
      <span class="contact__name">Lenny Firth</span>
      <span class="contact__phone">0472 316 508</span>
      <span class="contact__email">lfirth@critterloop.com.au</span>
      <span class="contact__social">FB/lenny.firth.263</span>
      <span class="contact__web">StableArc.com.au</span>
    </address>
  </main>
</body>
</html>
```